Software Development Consulting Company Needs Business Card Design

We need a new business card design for our consultants at Marendo Solutions (marendosolutions.example). We are a small firm that provides high-end software development and methodology consulting to medium to large enterprise IT organizations.

Our logo uses Futura for the font and we would like to stick with navy blue and canary yellow for the logo colors. Attached are normal and reversed versions of our logos in illustrator format.
Updates

Hi Everyone, Thank yo very much for your amazing design ideas. I have created a poll for this project and our employees will be voting on the design they wish to use. We will be making a decision this Wednesday (October 22nd). Thanks again, Gavin Hartwell

Industry/Entity Type

Business

```html
<!DOCTYPE html>
<html lang="en">
<head>
<meta charset="utf-8">
<title>Marendo Solutions – Business Card</title>
<link rel="stylesheet" href="https://fonts.googleapis.com/css2?family=Jost:wght@400;500&family=Open+Sans:wght@400;600;700&display=swap">
<style>
  :root {
    --navy: #23476b;
    --canary: #ffe500;
    --paper: #ffffff;
    --backdrop: #ececec;
    --muted: #8fa3b8;
    --ink-light: #ffffff;
  }
  * { box-sizing: border-box; margin: 0; padding: 0; }
  html, body {
    width: 1200px; height: 720px; overflow: hidden;
    background: var(--backdrop);
  }
  .stage {
    position: relative; width: 1200px; height: 720px;
    display: flex; align-items: center; justify-content: center; gap: 60px;
  }
  .card {
    position: relative; width: 520px; height: 297px; overflow: hidden;
    box-shadow: 0 6px 18px rgba(0,0,0,0.12);
    font-family: "Open Sans", Arial, sans-serif;
  }

  /* Back of card */
  .card--back { background: var(--navy); }
  .back-brand {
    position: absolute; left: 70px; top: 150px;
    display: flex; align-items: center; gap: 14px;
  }
  .back-brand__dot {
    width: 30px; height: 30px; border-radius: 50%; background: var(--canary);
  }
  .back-brand__name {
    font-family: "Jost", Futura, sans-serif; font-weight: 400;
    font-size: 26px; letter-spacing: 5px; text-transform: uppercase;
    color: var(--ink-light);
  }
  .back-info {
    position: absolute; right: 38px; top: 40px; text-align: right;
  }
  .back-info__company { font-size: 11px; color: var(--muted); }
  .back-info__web { font-size: 13px; font-weight: 700; color: var(--ink-light); }
  .back-info__web span { color: var(--canary); }

  /* Front of card */
  .card--front { background: var(--paper); }
  .front-shape { position: absolute; inset: 0; width: 520px; height: 297px; }
  .front-brand {
    position: absolute; left: 30px; top: 122px;
    display: flex; align-items: center; gap: 10px;
  }
  .front-brand__dot {
    width: 10px; height: 10px; border-radius: 50%; background: var(--canary);
  }
  .front-brand__name {
    font-family: "Jost", Futura, sans-serif; font-weight: 400;
    font-size: 15px; line-height: 19px; letter-spacing: 3px; text-transform: uppercase;
    color: var(--navy);
  }
  .front-brand__name span { display: block; }
  .contact {
    position: absolute; right: 22px; top: 34px; text-align: right;
    color: var(--ink-light);
  }
  .contact__name { font-size: 21px; font-weight: 700; line-height: 1.1; }
  .contact__title { font-size: 12px; color: var(--canary); margin-bottom: 18px; }
  .contact__line {
    display: flex; justify-content: flex-end; align-items: center; gap: 7px;
    font-size: 11.5px; line-height: 19px;
  }
  .contact__line--plain { padding-right: 19px; }
  .contact__icon { width: 12px; height: 12px; flex: none; }
</style>
</head>
<body>
<main class="stage">

  <section class="card card--back" aria-label="Card back">
    <div class="back-info">
      <p class="back-info__company">Marendo Solutions, LLC</p>
      <p class="back-info__web">www.<span>marendosolutions</span>.example</p>
    </div>
    <div class="back-brand">
      <span class="back-brand__dot"></span>
      <span class="back-brand__name">Marendo</span>
    </div>
  </section>

  <section class="card card--front" aria-label="Card front">
    <svg class="front-shape" viewBox="0 0 520 297" aria-hidden="true">
      <path d="M188,0 Q200,190 300,297 L330,297 Q232,190 222,0 Z" fill="var(--canary)"/>
      <path d="M222,0 Q232,190 330,297 L520,297 L520,0 Z" fill="var(--navy)"/>
    </svg>

    <div class="front-brand">
      <span class="front-brand__dot"></span>
      <p class="front-brand__name"><span>Marendo</span><span>Solutions</span></p>
    </div>

    <div class="contact">
      <p class="contact__name">Gavin Hartwell</p>
      <p class="contact__title">Principal Consultant</p>
      <p class="contact__line">gavin.hartwell@marendosolutions.example
        <svg class="contact__icon" viewBox="0 0 12 12"><rect x="0.7" y="2.2" width="10.6" height="7.6" fill="none" stroke="var(--canary)" stroke-width="1.1"/><path d="M0.7,2.4 L6,6.6 L11.3,2.4" fill="none" stroke="var(--canary)" stroke-width="1.1"/></svg>
      </p>
      <p class="contact__line">555-201-4387
        <svg class="contact__icon" viewBox="0 0 12 12"><rect x="3" y="0.6" width="6" height="10.8" rx="1" fill="none" stroke="var(--canary)" stroke-width="1.1"/><circle cx="6" cy="9.4" r="0.7" fill="var(--canary)"/></svg>
      </p>
      <p class="contact__line">555-201-4390
        <svg class="contact__icon" viewBox="0 0 12 12"><path d="M2.6,1 L4.6,1 L5.4,3.6 L4,4.6 Q5,7 7.4,8 L8.4,6.6 L11,7.4 L11,9.4 Q10.6,11 8.6,11 Q1,10 1,3 Q1,1.2 2.6,1 Z" fill="var(--canary)"/></svg>
      </p>
      <p class="contact__line">2240 Harbor Ridge Dr.,
        <svg class="contact__icon" viewBox="0 0 12 12"><path d="M6,11.4 Q1.8,6.6 1.8,4.4 A4.2,4.2 0 0 1 10.2,4.4 Q10.2,6.6 6,11.4 Z" fill="var(--canary)"/><circle cx="6" cy="4.4" r="1.5" fill="var(--navy)"/></svg>
      </p>
      <p class="contact__line contact__line--plain">Fenwick, MO 63190</p>
    </div>
  </section>

</main>
</body>
</html>
```